Square Business Cards for Our Restaurant / Event Venue

We need square business cards designed for the management team of our event venue and restaurant. On one side of the card should be the the Harbor Lantern 7 logo and URL www.harborlantern7.example. On the other side should be the Ember Logo and URL www.emberhall7.example. All employee details should be on the side with Ember logo. There will be a total of 5 cards to be created with the design.

Clara Bennquist
clara@harborlantern7.example

main 555.418.3072
direct 555.730.2946

4831 West Orchard Lane SE
Washington, DC 90417

Industry/Entity Type

Business

```html
<!DOCTYPE html>
<html lang="en">
<head>
<meta charset="utf-8">
<title>Harbor Lantern 7 – Square Business Cards</title>
<link rel="stylesheet" href="https://fonts.googleapis.com/css2?family=Montserrat:wght@300;400;600;700&display=swap">
<style>
  :root {
    --backdrop: #e9e9e9;
    --card: #141213;
    --ink-light: #ffffff;
    --accent: #b3201f;
  }
  * { box-sizing: border-box; margin: 0; padding: 0; }
  html, body {
    width: 1200px;
    height: 800px;
    overflow: hidden;
    background: var(--backdrop);
    font-family: "Montserrat", sans-serif;
  }
  .canvas {
    position: relative;
    width: 1200px;
    height: 800px;
  }
  .card {
    position: absolute;
    top: 170px;
    width: 460px;
    height: 460px;
    background: var(--card);
    box-shadow: 0 6px 18px rgba(0, 0, 0, 0.18);
  }
  .card--contact { left: 110px; }
  .card--brand { left: 630px; }

  /* Contact side */
  .contact {
    position: absolute;
    left: 52px;
    top: 52px;
    right: 40px;
    color: var(--ink-light);
  }
  .contact__brand {
    display: flex;
    align-items: center;
    gap: 12px;
    font-size: 64px;
    font-weight: 700;
    line-height: 1;
    letter-spacing: -1px;
  }
  .contact__brand-dot {
    width: 14px;
    height: 14px;
    border-radius: 50%;
    background: var(--accent);
  }
  .contact__name {
    margin-top: 36px;
    font-size: 19px;
    font-weight: 600;
    letter-spacing: 0.5px;
    text-transform: uppercase;
  }
  .contact__line {
    font-size: 15px;
    font-weight: 300;
    line-height: 1.5;
  }
  .contact__line--first { margin-top: 4px; }
  .contact__divider {
    width: 6px;
    height: 6px;
    border-radius: 50%;
    background: var(--accent);
    margin: 10px 0 10px 80px;
  }

  /* Shared URL line */
  .card__url {
    position: absolute;
    left: 0;
    right: 0;
    bottom: 58px;
    text-align: center;
    color: var(--accent);
    font-size: 16px;
    font-weight: 400;
    letter-spacing: 0.8px;
  }

  /* Brand side */
  .brand {
    position: absolute;
    inset: 0;
    display: flex;
    flex-direction: column;
    align-items: center;
  }
  .brand__mark {
    margin-top: 170px;
    display: flex;
    align-items: center;
    gap: 14px;
    color: var(--accent);
    font-size: 38px;
    font-weight: 400;
    letter-spacing: 0.5px;
  }
  .brand__mark-dot {
    width: 22px;
    height: 22px;
    border-radius: 50%;
    background: var(--accent);
  }
</style>
</head>
<body>
<main class="canvas">
  <section class="card card--contact" aria-label="Card back with contact details">
    <div class="contact">
      <div class="contact__brand">
        <span class="contact__brand-name">Ember</span>
        <span class="contact__brand-dot" aria-hidden="true"></span>
      </div>
      <p class="contact__name">Clara Bennquist</p>
      <p class="contact__line contact__line--first">clara@harborlantern7.example</p>
      <div class="contact__divider" aria-hidden="true"></div>
      <p class="contact__line">main 555.418.3072</p>
      <p class="contact__line">direct 555.730.2946</p>
      <div class="contact__divider" aria-hidden="true"></div>
      <p class="contact__line">4831 West Orchard Lane SE</p>
      <p class="contact__line">Washington, DC 90417</p>
    </div>
    <p class="card__url">www.emberhall7.example</p>
  </section>

  <section class="card card--brand" aria-label="Card front with venue name">
    <div class="brand">
      <div class="brand__mark">
        <span class="brand__mark-dot" aria-hidden="true"></span>
        <span class="brand__mark-name">Harbor Lantern 7</span>
      </div>
    </div>
    <p class="card__url">www.harborlantern7.example</p>
  </section>
</main>
</body>
</html>
```